Company notecard redesign

We'd like a redesign done of our company notecards. We use these cards to hand-write messages to clients/potential clients. This could be thank-you cards, congratulations cards, check-in cards, etc. Current cards are 5.5" x 8.5" and fold in half (you'll see the fold mark on the scanned image). We would like the new cards to not fold, and just be 5.5" x 4.25". We do like the little dog head you'll see on the inside notecard scan as the dog is our logo. I've also attached our "professional" logo with our new tagline. Address info you see on the outside notecard scan is correct.

Target Market(s)

Brindlequay and CRM clients

Industry/Entity Type

It Company

Colors
3377b5
ffffff
fff8ef

Requirements
Must have
• Our logo, some contact info
Nice to have
• Dog head from our current notecard scan

```html
<!DOCTYPE html>
<html lang="en">
<head>
<meta charset="utf-8">
<title>Halden Notecard</title>
<link rel="stylesheet" href="https://fonts.googleapis.com/css2?family=Open+Sans:wght@400;700&family=Cormorant+SC:wght@600&display=swap">
<style>
  :root {
    --brand-blue: #3377b5;
    --navy: #1f2d5c;
    --paper: #ffffff;
    --mascot-tint: #e6ebf5;
  }
  html, body {
    margin: 0;
    padding: 0;
    overflow: hidden;
    background: var(--paper);
  }
  .notecard {
    position: relative;
    width: 929px;
    height: 1200px;
    box-sizing: border-box;
    border: 1.5px solid var(--navy);
    background: var(--paper);
    overflow: hidden;
  }
  .notecard__frame {
    position: absolute;
    left: 29px;
    top: 29px;
    width: 871px;
    height: 1141px;
    box-sizing: border-box;
    border: 4.5px solid var(--navy);
  }
  .brand {
    position: absolute;
    left: 61px;
    top: 48px;
    margin: 0;
  }
  .brand__name {
    display: block;
    font-family: "Open Sans", Arial, sans-serif;
    font-weight: 700;
    font-size: 108px;
    line-height: 1;
    letter-spacing: 2px;
    text-transform: uppercase;
    color: var(--brand-blue);
  }
  .brand__tagline {
    display: block;
    margin-top: 24px;
    font-family: "Open Sans", Arial, sans-serif;
    font-weight: 400;
    font-size: 23px;
    line-height: 1;
    letter-spacing: 5.6px;
    text-transform: uppercase;
    color: var(--brand-blue);
  }
  .mascot {
    position: absolute;
    left: 152px;
    top: 305px;
    width: 591px;
    height: 598px;
  }
  .contact {
    position: absolute;
    top: 1052px;
    font-family: "Cormorant SC", Georgia, serif;
    font-weight: 600;
    font-size: 34px;
    line-height: 47px;
    color: var(--navy);
    margin: 0;
  }
  .contact--web { left: 126px; text-align: left; }
  .contact--address { right: 126px; text-align: right; }
  .contact span { display: block; }
</style>
</head>
<body>
  <main class="notecard">
    <div class="notecard__frame"></div>

    <header class="brand">
      <span class="brand__name">Halden</span>
      <span class="brand__tagline">A Cloud Consulting Company</span>
    </header>

    <svg class="mascot" role="img" aria-label="Faint company mascot artwork belongs here" viewBox="0 0 591 598">
      <rect x="0" y="0" width="591" height="598" rx="120" fill="var(--mascot-tint)"/>
    </svg>

    <p class="contact contact--web">
      <span>haldentech.com</span>
      <span>555.041.2910</span>
    </p>
    <p class="contact contact--address">
      <span>1180 W. 48th Street</span>
      <span>Fairhaven, IN 46000</span>
    </p>
  </main>
</body>
</html>
```